Bright Path Flyer Design for Virtual Online Clinic. -5.5 x 8.5 inches (half sheet)

We need a clean, modern flyer design for Bright Path, a new virtual walk-in clinic based in British Columbia. The flyer will be used in libraries, pharmacies, and community centers to help residents easily access primary care through their Bright Path NFC access card.
The flyer will ask a question : NEED A DOCTOR? This should be large and attention grabbing.
The design should clearly feature a Bright Path card image (the access card) as the centerpiece and visually show how patients can use it to book appointments. The tone should feel trustworthy, healthcare-oriented, and community-friendly — clean fonts, clear spacing, and strong readability from a distance.

Side One: This card has the NFC Access Card.
NEED A DOCTOR? (Large Font, Attention Grabbing)
How to Book an Appointment using your Bright Path Card
Step 1: Tap Your Card on Your Phone
Hold your card near the back of your phone.
It will activate automatically — no app needed.
The Bright Path scheduler will open.
Step 2: Schedule Your Appointment
Select your clinical concern.
Choose your time window.
Register (only once).
Confirm your appointment.
Step 3: Relax, we’ll take care of the rest
A doctor will call during your scheduled time.
Once booked, you’ll be able to call our office.
No emails, no texts — just a real person.
It’s that simple.
Side Two:
About Bright Path
Created by Dr. Marcus Ferrigan
Bright Path was founded to make healthcare simple and convenient. Prescription renewals. Common infections. Medical notes. And so much more.
Our doctors can address 120+ health concerns virtually — providing quality care without the waiting room. No waiting rooms. Just real doctors providing real care.
Why Patients Choose Bright Path
Easy access – book and be seen from anywhere in BC.
Effortless booking – tap your Bright Path Card to begin.
Trusted physicians – every visit is with a licensed BC family doctor.
How It Works
Book your visit — choose a time window that fits your day.
Join the queue — you’ll be called when it’s your turn.
Speak directly with your doctor — simple, secure, and stress-free.
Convenient Care for Common Concerns

Additional Details.
Please find the domain to be launched soon. I've attached the NFC card file for review, it is 85.5 mm x 54 mm. The card will be glued to the flyer.
I've attached examples of flyers but they are not the look I am seeking and I am looking for creative solutions.
Thank you!
http://brightpath-example.test/

Adult Patients in British Columbia

Healthcare

• Looking for clean lines, uniform appearance, and high legibility i.e poppins

0054AA
0677BA
7BADD7
CADEEF
E8F1F8

• Need A Doctor?
• Elegant style, not too busy, clear layout.
• Clutter, look cheap - review examples.

```html
<!DOCTYPE html>
<html lang="en">
<head>
<meta charset="utf-8">
<title>Bright Path Flyer</title>
<link rel="stylesheet" href="https://fonts.googleapis.com/css2?family=Poppins:wght@400;500;600;700;800&display=swap">
<style>
  :root{
    --navy:#1f3f86;
    --blue:#0054AA;
    --blue-mid:#0677BA;
    --indigo:#2b2a8e;
    --yellow:#f7cf1a;
    --bg:#dcdcdc;
    --white:#ffffff;
    --card:#c9d3e6;
  }
  *{margin:0;padding:0;box-sizing:border-box}
  html,body{width:729px;height:1200px;overflow:hidden}
  body{background:var(--bg);position:relative;font-family:"Poppins",sans-serif;color:var(--indigo)}
  .page{position:absolute;top:47px;width:325px;height:502px;background:var(--white);overflow:hidden}
  .page--about{left:31px}
  .page--booking{left:373px}
  .header-band{position:absolute;left:0;top:0;width:100%;height:117px}
  .header-band svg{display:block;width:100%;height:100%}
  .header-rule{position:absolute;left:0;top:117px;width:100%;height:4px;background:var(--yellow)}
  .footer-rule{position:absolute;left:0;top:480px;width:100%;height:3px;background:var(--yellow)}
  .footer-band{position:absolute;left:0;top:483px;width:100%;height:19px;background:linear-gradient(90deg,var(--navy),var(--blue) 60%,var(--blue-mid))}
  .centered{position:absolute;left:0;width:100%;text-align:center}
  .brand-name{top:38px;color:var(--white);font-size:12px;font-weight:500;letter-spacing:.5px}
  .page-title{top:72px;color:var(--white);font-size:24px;font-weight:700}
  .intro-box{position:absolute;left:9px;top:144px;width:307px;height:71px;border:1px solid var(--indigo)}
  .intro-box__label{position:absolute;left:0;width:100%;text-align:center}
  .intro-box__label span{background:var(--white);padding:0 5px}
  .intro-box__label--top{top:-8px;font-size:10px;font-weight:400}
  .intro-box__label--top b{font-weight:600}
  .intro-box__label--bottom{bottom:-6px;font-size:7px}
  .intro-box__body{position:absolute;left:6px;right:6px;top:6px;text-align:center;font-size:7px;line-height:9.8px}
  .intro-box__body b{font-weight:600}
  .section-title{font-size:13.5px;font-weight:700}
  .check-line{font-size:9.2px;font-weight:500;white-space:nowrap}
  .check-line--wide{letter-spacing:1px}
  .tick{display:inline-block;position:relative;width:9px;height:9px;border-radius:50%;background:var(--yellow);vertical-align:-1px;margin-right:6px}
  .tick::after{content:"";position:absolute;left:3px;top:1.3px;width:2.5px;height:4.5px;border:solid var(--white);border-width:0 1.3px 1.3px 0;transform:rotate(40deg)}
  .tick--after{margin-right:0;margin-left:6px}
  .divider{position:absolute;height:2px;background:var(--yellow)}
  .headline{top:20px;color:var(--white);font-size:33px;font-weight:800;letter-spacing:.3px}
  .access-card{position:absolute;left:85px;top:64px;width:155px;height:96px;border-radius:6px 6px 0 0;border:4px solid var(--white);border-bottom:0;background:linear-gradient(135deg,var(--card),#e8f1f8)}
  .booking-banner{position:absolute;left:16px;top:177px;width:296px;height:41px;background:var(--blue);box-shadow:3px 3px 0 var(--yellow);color:var(--white);font-size:13px;font-weight:700;line-height:16.5px;text-align:center;padding-top:4px}
  .step{position:absolute;left:16px;right:12px}
  .step__title{font-size:12.8px;font-weight:700;white-space:nowrap}
  .step__list{list-style:none;margin-top:1px}
  .step__list li{font-size:9.3px;line-height:14.8px;padding-left:10px;white-space:nowrap;letter-spacing:.3px}
  .step--right{text-align:right}
  .step--right .step__list li{padding-left:0;padding-right:10px}
  .site-url{top:484px;color:var(--white);font-size:9.5px;letter-spacing:.5px}
</style>
</head>
<body>

  <section class="page page--about">
    <div class="header-band">
      <svg viewBox="0 0 325 117" preserveAspectRatio="none" aria-hidden="true">
        <rect width="325" height="117" fill="#233f80"/>
        <path d="M0 40 C90 70 200 20 325 55 V117 H0Z" fill="#0054AA"/>
        <path d="M170 0 C230 30 280 20 325 10 V0Z" fill="#0054AA" opacity=".7"/>
        <path d="M0 90 C120 105 220 70 325 95 V117 H0Z" fill="#0677BA" opacity=".6"/>
      </svg>
    </div>
    <div class="header-rule"></div>
    <p class="centered brand-name">Bright Path</p>
    <h1 class="centered page-title">About Bright Path</h1>

    <div class="intro-box">
      <p class="intro-box__label intro-box__label--top"><span>Created by <b>Dr. Marcus Ferrigan</b></span></p>
      <p class="intro-box__body">Bright Path was founded to make healthcare simple and convenient.<br><br><b>Prescription renewals. Common infections. Medical notes.</b> And so much more.<br>Our doctors can address <b>120+ health concerns</b> virtually — providing quality care without the waiting room.</p>
      <p class="intro-box__label intro-box__label--bottom"><span>No waiting rooms. Just real doctors providing real care.</span></p>
    </div>

    <h2 class="centered section-title" style="top:242px">Why Patients Choose Bright Path</h2>
    <p class="centered check-line" style="top:271px"><i class="tick"></i>Book and be seen from anywhere in BC.</p>
    <p class="centered check-line check-line--wide" style="top:294px"><i class="tick"></i>Tap your Bright Path Card to begin.</p>
    <p class="centered check-line" style="top:316px"><i class="tick"></i>Every visit is with a licensed BC Family Doctor.</p>

    <div class="divider" style="left:18px;width:289px;top:354px"></div>

    <h2 class="centered section-title" style="top:364px">How It Works</h2>
    <p class="centered check-line" style="top:390px"><i class="tick"></i>Choose a time window that fits your day.</p>
    <p class="centered check-line check-line--wide" style="top:412px"><i class="tick"></i>You’ll be called when it’s your turn.</p>
    <p class="centered check-line check-line--wide" style="top:435px"><i class="tick"></i>Simple, secure and stress-free.</p>

    <h2 class="centered section-title" style="top:455px">Convenient Care for Common Concerns</h2>

    <div class="footer-rule"></div>
    <div class="footer-band"></div>
  </section>

  <section class="page page--booking">
    <div class="header-band">
      <svg viewBox="0 0 325 117" preserveAspectRatio="none" aria-hidden="true">
        <rect width="325" height="117" fill="#233f80"/>
        <path d="M0 30 C100 60 200 10 325 45 V117 H0Z" fill="#0054AA"/>
        <path d="M220 0 C260 20 300 18 325 12 V0Z" fill="#0677BA" opacity=".7"/>
        <path d="M0 85 C120 100 220 65 325 90 V117 H0Z" fill="#0677BA" opacity=".5"/>
      </svg>
    </div>
    <div class="header-rule"></div>
    <h1 class="centered headline">NEED A DOCTOR?</h1>
    <div class="access-card" role="img" aria-label="Bright Path NFC access card, attached to the flyer"></div>

    <div class="booking-banner">How to Book an Appointment using your<br>Bright Path Card</div>

    <div class="step" style="top:231px">
      <h2 class="step__title">STEP 1: TAP YOUR CARD ON YOUR PHONE</h2>
      <ul class="step__list">
        <li><i class="tick"></i>Hold your card near the back of your phone.</li>
        <li><i class="tick"></i>It will activate automatically — no app needed.</li>
        <li><i class="tick"></i>The Bright Path scheduler will open.</li>
      </ul>
    </div>

    <div class="divider" style="left:18px;width:290px;top:299px"></div>

    <div class="step step--right" style="top:304px;right:2px">
      <h2 class="step__title">STEP 2: SCHEDULE YOUR APPOINTMENT</h2>
      <ul class="step__list">
        <li>Select your clinical concern<i class="tick tick--after"></i></li>
        <li>Choose your time window<i class="tick tick--after"></i></li>
        <li>Register (only once)<i class="tick tick--after"></i></li>
        <li>Confirm your appointment<i class="tick tick--after"></i></li>
      </ul>
    </div>

    <div class="divider" style="left:18px;width:290px;top:387px"></div>

    <div class="step" style="top:394px">
      <h2 class="step__title">STEP 3: RELAX, WE’LL TAKE CARE OF THE REST</h2>
      <ul class="step__list">
        <li><i class="tick"></i>Select your clinical concern</li>
        <li><i class="tick"></i>Choose your time window</li>
        <li><i class="tick"></i>Register (only once)</li>
        <li><i class="tick"></i>Confirm your appointment</li>
      </ul>
    </div>

    <div class="footer-rule"></div>
    <div class="footer-band"></div>
    <p class="centered site-url">brightpath-example.test</p>
  </section>

</body>
</html>
```